Nobody Left the Lantern Burning - Tom Halvery - CD Cover Design Project

Single Cover for CD & Online media e.g. Tunebox Graphics
The first song release from Tom Halvery will be the track 'Nobody Left the Lantern Burning'.
For the release the single requires artwork that is eye catching, seriously professional & meets the requirements of Disc Sprout, Tunebox and also a physical copy on CD.
Track listings for CD will be:
1. Nobody Left the Lantern Burning
2. Nobody Left the Lantern Burning - Instrumental
see details in this link:
http://members.discsprout-example.com/faq.aspx
http://selfmadesound.discsprout-example.com/2009/11/avoid-album-art-atrocities/
http://answers.quorvex-example.com/question/index?qid=20111015141433AAdDTmH
Any advice on this would be greatly appreciated,
I would also like the two logo's I have uploaded to be used,
one is the Tom Halvery logo and the other is for Milbrook & Tandy Records logo (please remove the R and replace with a C for copyright.)
There are four high res photo shopped pictures of Tom Halvery and another zip file of many others, it would be nice to include one of these maybe on the 2nd page or back of the CD. Please don't use them as the front cover.
I imagine an Art Deco illustration but please listen to the track and let it inspire you.
Good Luck
Updates
I don't feel this is what I'm looking for, the design needs to refelct a broken heart without being a picture of a broken heart
Reason: No design has been what we are after so far so the deadline has been extended and the budget increased.

```html
<!DOCTYPE html>
<html lang="en">
<head>
<meta charset="utf-8">
<title>Tom Halvery – Nobody Left the Lantern Burning – CD Cover</title>
<link rel="stylesheet" href="https://fonts.googleapis.com/css2?family=Roboto:wght@700;900&family=Roboto+Condensed:wght@400;700&display=swap">
<style>
  :root {
    --navy: #120c2e;
    --navy-deep: #0b0720;
    --ember: #d2381a;
    --amber: #f28a1e;
    --gold: #ffd36b;
    --glow: #fff3c8;
    --ink: #ffffff;
    --dieline: rgba(255, 255, 255, 0.35);
  }
  * { margin: 0; padding: 0; box-sizing: border-box; }
  html, body {
    width: 1200px; height: 585px; overflow: hidden;
    background: #ffffff;
  }
  .cover-spread {
    position: relative;
    width: 1200px; height: 585px;
    overflow: hidden;
    font-family: "Roboto", Arial, sans-serif;
    color: var(--ink);
  }
  .panel {
    position: absolute; top: 0; height: 585px; overflow: hidden;
    background:
      linear-gradient(100deg, transparent 30%, rgba(255, 211, 107, 0.35) 45%, transparent 55%),
      linear-gradient(78deg, transparent 35%, rgba(255, 243, 200, 0.55) 50%, transparent 60%),
      linear-gradient(120deg, transparent 25%, rgba(242, 138, 30, 0.55) 42%, transparent 60%),
      radial-gradient(ellipse 55% 70% at 55% 60%, rgba(255, 190, 90, 0.85), rgba(210, 56, 26, 0.75) 45%, rgba(18, 12, 46, 0) 80%),
      linear-gradient(180deg, var(--navy) 0%, #3a1230 55%, var(--navy) 100%);
  }
  .panel--back { left: 0; width: 586px; }
  .panel--front { left: 615px; width: 585px; }

  .spine {
    position: absolute; left: 586px; top: 0;
    width: 29px; height: 585px;
    background: var(--navy-deep);
  }
  .spine__text {
    position: absolute; left: 50%; top: 18px;
    transform-origin: 0 0;
    transform: rotate(90deg) translateY(-50%);
    white-space: nowrap;
    font-family: "Roboto Condensed", Arial, sans-serif;
    font-weight: 400; font-size: 14px; letter-spacing: 0.5px;
    line-height: 1;
  }
  .spine__title { margin-left: 90px; }

  .artist-mark { position: absolute; text-transform: uppercase; line-height: 0.9; }
  .artist-mark__first { display: block; font-weight: 900; }
  .artist-mark__last { display: block; font-weight: 700; }
  .artist-mark__single {
    display: block;
    font-family: "Roboto Condensed", Arial, sans-serif;
    font-weight: 400; letter-spacing: 0.3px;
  }
  .panel--back .artist-mark { left: 195px; top: 226px; }
  .panel--back .artist-mark__first { font-size: 76px; }
  .panel--back .artist-mark__last { font-size: 44px; margin-top: 6px; }
  .panel--back .artist-mark__single { font-size: 12px; margin-top: 6px; }
  .panel--front .artist-mark { left: 52px; top: 34px; z-index: 2; }
  .panel--front .artist-mark__first { font-size: 72px; }
  .panel--front .artist-mark__last { font-size: 42px; margin-top: 6px; }
  .panel--front .artist-mark__single { font-size: 12px; margin-top: 6px; }

  .track-list {
    position: absolute; left: 25px; top: 486px;
    font-family: "Roboto Condensed", Arial, sans-serif;
    font-size: 11px; line-height: 14px; text-transform: uppercase;
    list-style: none;
  }
  .track-list__heading { font-weight: 700; }

  .label-mark {
    position: absolute;
    display: flex; flex-direction: column; align-items: center; gap: 4px;
    font-family: "Roboto Condensed", Arial, sans-serif;
    font-weight: 700; font-size: 7px; text-transform: uppercase;
    letter-spacing: 0.3px; text-align: center; width: 80px;
  }
  .label-mark__dot {
    width: 26px; height: 26px; border-radius: 50%;
    background: var(--ember);
  }
  .panel--back .label-mark { left: 469px; top: 490px; }
  .panel--front .label-mark { left: 35px; top: 522px; }

  .artist-portrait {
    position: absolute; left: 208px; top: 56px;
    width: 377px; height: 529px;
    background:
      radial-gradient(ellipse 45% 30% at 45% 22%, rgba(122, 74, 40, 0.95), rgba(122, 74, 40, 0) 70%),
      radial-gradient(ellipse 40% 28% at 40% 48%, rgba(232, 170, 120, 0.9), rgba(232, 170, 120, 0) 75%),
      linear-gradient(180deg, rgba(255, 255, 255, 0) 55%, rgba(245, 240, 236, 0.95) 80%);
  }

  .dielines { position: absolute; inset: 0; pointer-events: none; }
</style>
</head>
<body>
<main class="cover-spread">
  <section class="panel panel--back" aria-label="Back cover">
    <div class="artist-mark">
      <span class="artist-mark__first">Tom</span>
      <span class="artist-mark__last">Halvery</span>
      <span class="artist-mark__single">Nobody Left the Lantern Burning</span>
    </div>
    <ul class="track-list">
      <li class="track-list__heading">Songs:</li>
      <li>1. Nobody Left the Lantern Burning</li>
      <li>2. Nobody Left the Lantern Burning - Instrumental</li>
    </ul>
    <div class="label-mark">
      <span class="label-mark__dot"></span>
      <span class="label-mark__name">Milbrook &amp; Tandy Records</span>
    </div>
  </section>

  <aside class="spine" aria-label="Spine">
    <p class="spine__text">
      <span class="spine__artist">TOM HALVERY</span>
      <span class="spine__title">NOBODY LEFT THE LANTERN BURNING</span>
    </p>
  </aside>

  <section class="panel panel--front" aria-label="Front cover">
    <div class="artist-portrait" role="img" aria-label="Portrait photograph of the artist in a white shirt and glasses, lit by warm orange light"></div>
    <div class="artist-mark">
      <span class="artist-mark__first">Tom</span>
      <span class="artist-mark__last">Halvery</span>
      <span class="artist-mark__single">Nobody Left the Lantern Burning</span>
    </div>
    <div class="label-mark">
      <span class="label-mark__dot"></span>
      <span class="label-mark__name">Milbrook &amp; Tandy Records</span>
    </div>
  </section>

  <svg class="dielines" width="1200" height="585" viewBox="0 0 1200 585" aria-hidden="true">
    <g fill="none" stroke="var(--dieline)" stroke-width="1">
      <path d="M0 62 L140 20 L470 20 L586 62"/>
      <path d="M615 62 L730 20 L1060 20 L1200 62"/>
      <path d="M0 575 L586 575"/>
      <path d="M615 575 L1200 575"/>
    </g>
  </svg>
</main>
</body>
</html>
```